Business Card for a Renewable energy construction company

I need a formal, neat looking business card. Minimal and professional looking. Back side can have a design that is semi-ransparent/shaded

Target Market(s)

Renewable energy companies

Contact Information for Business Card

Name, Surname and contact details (phone, email)

Colors
00AB8E
00BBA5
67D7C9
C6EFE9
E9F9F6

Requirements
Must have
• Place for a QR code in the back side

```html
<!DOCTYPE html>
<html lang="en">
<head>
<meta charset="utf-8">
<title>Norvell – Business Card</title>
<link rel="stylesheet" href="https://fonts.googleapis.com/css2?family=Montserrat:wght@400;500;700&family=Oswald:wght@600&display=swap">
<style>
  :root {
    --stage: #3a3b3d;
    --card: #141414;
    --card-back: #0d0d0d;
    --teal: #2a9a9c;
    --teal-light: #67d7c9;
    --ink: #f2f2f2;
  }
  * { margin: 0; padding: 0; box-sizing: border-box; }
  html, body { width: 1200px; height: 900px; overflow: hidden; }
  body {
    background: var(--stage);
    font-family: "Montserrat", sans-serif;
    color: var(--ink);
    position: relative;
  }
  .card {
    position: absolute;
    top: 118px;
    width: 380px;
    height: 665px;
    border-radius: 2px;
    box-shadow: 0 10px 30px rgba(0,0,0,.45);
  }
  .card--front { left: 180px; background: var(--card); }
  .card--back { left: 640px; background: var(--card-back); overflow: hidden; }

  .brand {
    position: absolute;
    top: 150px;
    left: 0; right: 0;
    text-align: center;
  }
  .brand__mark {
    display: inline-block;
    width: 30px; height: 30px;
    background: var(--teal);
    margin-bottom: 16px;
  }
  .brand__name {
    font-weight: 700;
    font-size: 52px;
    letter-spacing: 4px;
    color: var(--ink);
    line-height: 1;
  }
  .brand__tagline {
    margin-top: 10px;
    font-weight: 700;
    font-size: 10.5px;
    letter-spacing: 1.6px;
    text-transform: uppercase;
    color: var(--ink);
  }

  .person {
    position: absolute;
    top: 385px;
    left: 0; right: 0;
    text-align: center;
  }
  .person__name {
    font-family: "Oswald", sans-serif;
    font-weight: 600;
    font-size: 34px;
    letter-spacing: 1px;
    text-transform: uppercase;
    color: var(--teal);
    line-height: 1.1;
  }
  .person__title {
    font-size: 17px;
    letter-spacing: .5px;
    margin-top: 2px;
  }

  .contact-icons {
    position: absolute;
    top: 462px;
    left: 36px; right: 36px;
    display: flex;
    align-items: center;
    gap: 8px;
  }
  .contact-icons__rule { flex: 1; height: 2px; background: var(--teal); }
  .contact-icons__icon {
    width: 26px; height: 26px;
    background: var(--teal);
    display: flex; align-items: center; justify-content: center;
  }
  .contact-icons__icon svg { width: 15px; height: 15px; }

  .contact-list {
    position: absolute;
    top: 506px;
    left: 0; right: 0;
    text-align: center;
    font-size: 15.5px;
    line-height: 1.45;
    letter-spacing: .3px;
  }
  .divider {
    position: absolute;
    top: 582px;
    left: 60px; right: 60px;
    height: 2px;
    background: var(--teal);
  }
  .address {
    position: absolute;
    top: 598px;
    left: 0; right: 0;
    text-align: center;
    font-size: 15.5px;
    line-height: 1.35;
    letter-spacing: .3px;
  }

  .back-pattern {
    position: absolute;
    inset: 0;
    background:
      linear-gradient(160deg, rgba(160,160,160,.35) 0%, rgba(90,90,90,.2) 40%, rgba(0,0,0,0) 65%),
      var(--card-back);
  }
  .back-brand {
    position: absolute;
    right: 40px;
    bottom: 190px;
    font-weight: 700;
    font-size: 18px;
    letter-spacing: 2px;
    color: var(--teal);
  }
</style>
</head>
<body>
  <section class="card card--front">
    <header class="brand">
      <span class="brand__mark"></span>
      <div class="brand__name">NORVELL</div>
      <div class="brand__tagline">Building towards clean energy</div>
    </header>

    <div class="person">
      <div class="person__name">Daniel Whitford</div>
      <div class="person__title">Founder &amp; CEO</div>
    </div>

    <div class="contact-icons">
      <span class="contact-icons__rule"></span>
      <span class="contact-icons__icon" aria-label="Phone">
        <svg viewBox="0 0 24 24" fill="#fff"><path d="M6.6 10.8a15.1 15.1 0 0 0 6.6 6.6l2.2-2.2a1 1 0 0 1 1-.25 11.4 11.4 0 0 0 3.6.6 1 1 0 0 1 1 1V20a1 1 0 0 1-1 1A17 17 0 0 1 3 4a1 1 0 0 1 1-1h3.5a1 1 0 0 1 1 1 11.4 11.4 0 0 0 .6 3.6 1 1 0 0 1-.25 1z"/></svg>
      </span>
      <span class="contact-icons__icon" aria-label="Email">
        <svg viewBox="0 0 24 24" fill="none" stroke="#fff" stroke-width="2"><rect x="3" y="5" width="18" height="14" rx="1"/><path d="M3 6l9 7 9-7"/></svg>
      </span>
      <span class="contact-icons__icon" aria-label="Website">
        <svg viewBox="0 0 24 24" fill="none" stroke="#fff" stroke-width="1.8"><circle cx="12" cy="12" r="9"/><ellipse cx="12" cy="12" rx="4" ry="9"/><path d="M3 12h18M5 7h14M5 17h14"/></svg>
      </span>
      <span class="contact-icons__rule"></span>
    </div>

    <div class="contact-list">
      <div>(555) 214-3087</div>
      <div>info@norvellenergy.com</div>
      <div>www.norvellenergy.com</div>
    </div>

    <div class="divider"></div>

    <address class="address" style="font-style: normal;">
      2180 Ridgeview Parkway Austin,<br>TX 78741
    </address>
  </section>

  <section class="card card--back">
    <div class="back-pattern" role="img" aria-label="Glossy shaded pattern of repeated brand chevrons fading from light grey to black"></div>
    <div class="back-brand">NORVELL</div>
  </section>
</body>
</html>
```